Health Change Motivational Postcard

We are a practice of diet and exercise experts. We'd like a print and email postcard design to send people when they are having a hard time or haven't been in to see us for a while.
Our current design shows a mountain climber" holding the rope and looking up at the summit from half way and says "Changing your diet doesn't have to be an uphill battle. Drop me a line for some help" but we're looking for something new or a new perspective.

DL size would suit with the image and text on one side. The other side will be blank, and we'd like to be able to adapt the design for an email also.

Reason: To gather more ideas and share them with our team.

This is a sample of the current version.

Hi, I had a request to submit some potential text for a card, so I've found a few that feel appropriate. 

"Start where you are. Use what you have. Do what you can" - Milton Greve

"It does not matter how slowly you go as long as you do not stop" - Belvardius

"80% of success is showing up" - Percy Tolland

I'm going to extend the time on this project because nothing quite fits so far but I think there is good potential and would love to come out with something useable that. The people receiving this will have failed to attend an appointment for dietary change of some kind. They may have diabetes, they may have been trying to lose weight or have irritable bowel syndrome. Not showing up for an appt may mean they've slipped out of the system but could be doing ok, it could mean they're doing poorly or they've lost motivation. I want them to receive something thoughtful from me either by physical postcard or by purpose designed email. What feel would you like to the standardised part of the message if you were in that situation?

Thanks for your creativity. Regards Rosalie

Reason: I've extended the deadline because I've just provided more direction. I initially wanted something that was not influenced by my preconceptions but I think each of the designs I've received needs something to be meaningful to the potential receivers. Avoid images of perfect bodies because that may be alienating to the target audience.

• Our business colours are purple and green and so we'd like the design to complement that and will need to contain our logo too. The tone is light hearted but professional and respectful, something that will make them smile or appreciate the thought. Our website is www.tallwillow.net.au
• A suitable statement or slogan could be included.

```html
<!DOCTYPE html>
<html lang="en">
<head>
<meta charset="utf-8">
<title>Keep Climbing Postcard</title>
<link rel="stylesheet" href="https://fonts.googleapis.com/css2?family=Oswald:wght@300;400&family=Playfair+Display:ital@1&display=swap">
<style>
  :root {
    --scene-dark: #1c201d;
    --scene-mid: #343b36;
    --scene-light: #4a524b;
    --ink: #ecedea;
    --ink-soft: #dcdedb;
  }
  html, body {
    margin: 0;
    padding: 0;
    width: 1200px;
    height: 573px;
    overflow: hidden;
    background: var(--scene-dark);
  }
  .postcard {
    position: relative;
    width: 1200px;
    height: 573px;
    overflow: hidden;
  }
  .stairway-scene {
    position: absolute;
    inset: 0;
    background:
      radial-gradient(ellipse 70% 80% at 50% 45%, var(--scene-light) 0%, var(--scene-mid) 45%, var(--scene-dark) 100%);
  }
  .message {
    position: absolute;
    inset: 0;
    color: var(--ink);
    text-shadow: 0 2px 6px rgba(0,0,0,0.45);
  }
  .headline {
    position: absolute;
    left: 0;
    right: 0;
    top: 92px;
    margin: 0;
    text-align: center;
    font-family: "Oswald", sans-serif;
    font-weight: 300;
    font-size: 96px;
    line-height: 1;
    letter-spacing: 1px;
  }
  .headline .emphasis {
    position: relative;
  }
  .underline-double {
    position: absolute;
    left: 740px;
    top: 186px;
    width: 224px;
    height: 18px;
  }
  .subline {
    position: absolute;
    left: 0;
    right: 0;
    top: 232px;
    margin: 0;
    text-align: center;
    font-family: "Playfair Display", serif;
    font-style: italic;
    font-size: 58px;
    line-height: 1;
    color: var(--ink-soft);
  }
  .subline .cap-swash {
    font-size: 74px;
  }
  .closing {
    position: absolute;
    left: 0;
    right: 0;
    top: 356px;
    margin: 0;
    display: flex;
    justify-content: center;
    align-items: baseline;
    gap: 16px;
    font-family: "Oswald", sans-serif;
    font-weight: 400;
    font-size: 56px;
    line-height: 1;
  }
  .closing .lower {
    font-size: 46px;
  }
  .closing .highlight {
    font-size: 84px;
  }
  .closing .stop {
    display: inline-block;
    width: 11px;
    height: 11px;
    background: var(--ink);
    margin-left: 4px;
  }
</style>
</head>
<body>
  <main class="postcard">
    <div class="stairway-scene" role="img" aria-label="Dark photograph of stone steps climbing through lush jungle foliage"></div>
    <section class="message">
      <h1 class="headline">IT DOESN'T <span class="emphasis">MATTER</span></h1>
      <svg class="underline-double" viewBox="0 0 224 18" aria-hidden="true">
        <rect x="0" y="0" width="224" height="6" fill="#ecedea"/>
        <rect x="0" y="12" width="224" height="2.5" fill="#ecedea"/>
      </svg>
      <p class="subline">How Man<span class="cap-swash">Y</span> Steps it takes to get there</p>
      <p class="closing">
        <span>ASLON<span class="lower">g</span></span>
        <span><span class="lower">a</span>S</span>
        <span class="highlight">You</span>
        <span>KEEP</span>
        <span>CLIM<span class="lower">bi</span>NG<span class="stop"></span></span>
      </p>
    </section>
  </main>
</body>
</html>
```